Business card

would like a double sided business card made up with my logos provided.
Prefer card to have black background and to use the black logos, with matching blue writing for the text.
One side to just be the logo, (Try to use both the black logos)
the other side to have the logo and also my credentials/business information.

Covering all aspects of Carpentry and Building Services

Marcus Tolvey
Qualified Carpenter
Mob: 0417263948
Email: rkt.joinery@mailbright.com
ABN: 47 615 209 834

Industry/Entity Type

Business

Contact Information for Business Card

Marcus Tolvey
Qualified Carpenter
Mob: 0417263948
ABN: 47 615 209 834

Requirements
Must have
• Please try to use both the black logos and incorporate into the card.

```html
<!DOCTYPE html>
<html lang="en">
<head>
<meta charset="utf-8">
<title>RKT Joinery – Business Card</title>
<link href="https://fonts.googleapis.com/css2?family=Open+Sans:wght@400;600&family=Noto+Serif:wght@700&display=swap" rel="stylesheet">
<style>
  :root {
    --backdrop: #8d8f91;
    --card-black: #030303;
    --brand-blue: #3396cf;
    --line-blue: #2f8fd0;
    --ink-dark: #1d2a33;
    --ink-light: #f2f2f2;
    --logo-grey: #e4e4e4;
  }
  * { box-sizing: border-box; margin: 0; padding: 0; }
  html, body { width: 1200px; height: 1200px; overflow: hidden; }
  body {
    background: var(--backdrop);
    font-family: "Open Sans", Arial, sans-serif;
    position: relative;
  }
  .card {
    position: absolute;
    left: 160px;
    width: 880px;
    height: 503px;
    background: var(--card-black);
    overflow: hidden;
    box-shadow: 0 8px 24px rgba(0,0,0,.35);
  }
  .card--front { top: 64px; }
  .card--back { top: 633px; }

  /* Front */
  .rule {
    position: absolute;
    left: 140px;
    right: 140px;
    height: 3px;
    background: var(--line-blue);
  }
  .rule--top { top: 176px; }
  .rule--bottom { top: 330px; }
  .wordmark {
    position: absolute;
    display: flex;
    align-items: center;
    gap: 14px;
    font-weight: 600;
    letter-spacing: 2px;
    white-space: nowrap;
  }
  .wordmark__mark {
    width: 18px; height: 18px;
    background: var(--brand-blue);
  }
  .card--front .wordmark {
    top: 218px; left: 0; right: 0;
    justify-content: center;
    font-size: 60px;
    line-height: 72px;
    color: var(--logo-grey);
  }

  /* Back */
  .band {
    position: absolute;
    left: 0; right: 0;
    top: 36px;
    height: 200px;
    background: var(--brand-blue);
  }
  .card--back .wordmark {
    top: 86px; left: 0; right: 0;
    justify-content: center;
    font-size: 44px;
    line-height: 54px;
    color: var(--ink-dark);
  }
  .card--back .wordmark__mark { background: var(--ink-dark); width: 14px; height: 14px; }
  .tagline {
    position: absolute;
    top: 158px; left: 0; right: 0;
    text-align: center;
    font-size: 17px;
    color: var(--ink-dark);
  }
  .tagline-rule {
    position: absolute;
    top: 150px; left: 260px; right: 260px;
    height: 1px;
    background: linear-gradient(90deg, transparent, #cfe6f4, transparent);
  }
  .title-row {
    position: absolute;
    top: 236px; left: 0; right: 0;
    height: 40px;
    display: flex;
    justify-content: space-between;
    align-items: center;
    padding: 0 40px;
    color: var(--ink-light);
    font-size: 22px;
  }
  .title-row__name { font-size: 25px; }
  .title-row__role { font-size: 19px; }
  .accent-line {
    position: absolute;
    top: 276px; left: 0; right: 0;
    height: 9px;
    background: var(--brand-blue);
  }
  .contact {
    position: absolute;
    display: flex;
    flex-direction: column;
    align-items: center;
    gap: 10px;
    font-family: "Noto Serif", Georgia, serif;
    font-weight: 700;
    color: var(--ink-light);
    white-space: nowrap;
  }
  .contact__icon { width: 18px; height: 18px; }
  .contact--phone { top: 318px; left: 40px; font-size: 19px; }
  .contact--email { top: 352px; left: 260px; font-size: 20px; }
  .contact--abn { top: 390px; left: 600px; font-size: 20px; }
</style>
</head>
<body>

<section class="card card--front" aria-label="Business card front">
  <div class="rule rule--top"></div>
  <div class="wordmark"><span class="wordmark__mark"></span><span class="wordmark__name">RKT JOINERY</span></div>
  <div class="rule rule--bottom"></div>
</section>

<section class="card card--back" aria-label="Business card back">
  <div class="band"></div>
  <div class="wordmark"><span class="wordmark__mark"></span><span class="wordmark__name">RKT JOINERY</span></div>
  <div class="tagline-rule"></div>
  <p class="tagline">Covering all aspects of Carpentry and Building Services</p>

  <div class="title-row">
    <span class="title-row__name">Marcus Tolvey</span>
    <span class="title-row__role">Qualified Carpenter</span>
  </div>
  <div class="accent-line"></div>

  <div class="contact contact--phone">
    <svg class="contact__icon" viewBox="0 0 18 18" aria-hidden="true">
      <circle cx="9" cy="9" r="9" fill="#dcdcdc"/>
      <rect x="6" y="4" width="6" height="10" rx="1" fill="#222"/>
      <rect x="7" y="5.5" width="4" height="5" fill="#dcdcdc"/>
    </svg>
    <span>0417263948</span>
  </div>

  <div class="contact contact--email">
    <svg class="contact__icon" viewBox="0 0 18 18" aria-hidden="true">
      <circle cx="9" cy="9" r="9" fill="#dcdcdc"/>
      <rect x="4.5" y="6" width="9" height="6.5" fill="none" stroke="#222" stroke-width="1.2"/>
      <path d="M4.5 6 L9 9.8 L13.5 6" fill="none" stroke="#222" stroke-width="1.2"/>
    </svg>
    <span>rkt.joinery@mailbright.com</span>
  </div>

  <div class="contact contact--abn">
    <svg class="contact__icon" viewBox="0 0 18 18" aria-hidden="true">
      <circle cx="9" cy="9" r="9" fill="#dcdcdc"/>
      <path d="M9 4.5 V11 M6 8.5 L9 12 L12 8.5" fill="none" stroke="#222" stroke-width="1.8"/>
    </svg>
    <span>ABN: 47 615 209 834</span>
  </div>
</section>

</body>
</html>
```